Consulting company business cards

We have a base design, but would be willing to update. We have a new logo/"tag" that needs to be added. Current business card design is attached for reference into our "style."

Industry/Entity Type

Business

Contact Information for Business Card

Should contain name and title, office number, mobile number if appropriate, e-mail, website, physical address, and company logo.

Font styles to use
Other font styles liked:
• See current card design on GorvandBCard

Colors
0455a3
85acd3
aaaaaa

Requirements
Must have
• Our colors are navy blue, gray, and a lighter blue
Nice to have
• Design that I can easily drop in new names/titles as we hire employees.

```html
<!DOCTYPE html>
<html lang="en">
<head>
<meta charset="utf-8">
<title>Tessaro Business Card</title>
<link href="https://fonts.googleapis.com/css2?family=Bebas+Neue&family=Open+Sans:wght@400;600&display=swap" rel="stylesheet">
<style>
  :root {
    --navy: #03304f;
    --sky: #7eaecb;
    --ink: #444a50;
    --paper: #ffffff;
    --backdrop: #262626;
  }
  * { margin: 0; padding: 0; box-sizing: border-box; }
  html, body { width: 1200px; height: 987px; overflow: hidden; }
  body {
    background: var(--backdrop);
    position: relative;
    font-family: "Open Sans", sans-serif;
  }
  .card {
    position: absolute;
    left: 293px;
    width: 615px;
    height: 352px;
    border-radius: 21px;
    overflow: hidden;
  }
  .card-front { top: 125px; background: var(--paper); }
  .card-back { top: 510px; background: var(--navy); }

  /* Front: brand */
  .brand {
    position: absolute;
    left: 316px;
    top: 36px;
    width: 258px;
  }
  .brand-row { display: flex; align-items: center; gap: 10px; }
  .brand-name {
    font-family: "Bebas Neue", sans-serif;
    font-size: 72px;
    line-height: 1;
    letter-spacing: 3px;
    color: var(--navy);
  }
  .brand-dot {
    width: 44px; height: 44px;
    border-radius: 50%;
    background: var(--sky);
  }
  .brand-tagline {
    margin-top: 4px;
    font-size: 12.5px;
    letter-spacing: 1.6px;
    color: #707880;
    white-space: nowrap;
  }

  /* Front: person */
  .person { position: absolute; left: 39px; top: 184px; right: 41px; }
  .person-name {
    font-family: "Bebas Neue", sans-serif;
    font-size: 31px;
    line-height: 1;
    letter-spacing: 0.5px;
    color: var(--navy);
  }
  .person-title-row { display: flex; align-items: center; gap: 6px; margin-top: 2px; }
  .person-title {
    font-family: "Bebas Neue", sans-serif;
    font-size: 19px;
    letter-spacing: 0.5px;
    color: var(--sky);
  }
  .person-rule { flex: 1; height: 1.5px; background: var(--sky); }

  /* Front: contacts */
  .contact-list {
    position: absolute;
    left: 39px;
    top: 248px;
    list-style: none;
    font-size: 16px;
    color: var(--ink);
  }
  .contact-list li { display: flex; align-items: center; height: 23px; }
  .contact-list svg { width: 16px; height: 16px; margin-right: 10px; fill: var(--navy); }
  .address {
    position: absolute;
    right: 40px;
    top: 248px;
    text-align: right;
    font-size: 16px;
    line-height: 23px;
    color: var(--ink);
    font-style: normal;
  }
  .address .web { letter-spacing: 1px; }

  /* Front: bottom band */
  .band { position: absolute; left: 0; bottom: 0; width: 615px; height: 13px; }

  /* Back */
  .emblem {
    position: absolute;
    left: 203px;
    top: 80px;
    width: 187px;
    height: 187px;
    border-radius: 42% 48% 30% 38%;
    background: radial-gradient(circle at 45% 40%, #8ab7d2, var(--sky));
  }
  .back-web {
    position: absolute;
    left: 0; right: 0;
    top: 294px;
    text-align: center;
    font-size: 17px;
    letter-spacing: 4px;
    color: #ffffff;
  }
</style>
</head>
<body>
  <section class="card card-front">
    <div class="brand">
      <div class="brand-row">
        <span class="brand-name">TESSARO</span>
        <span class="brand-dot"></span>
      </div>
      <p class="brand-tagline">A CLOUD CONSULTING COMPANY</p>
    </div>

    <div class="person">
      <h1 class="person-name">DANA WHITCOMBE</h1>
      <div class="person-title-row">
        <span class="person-title">OFFICE MANAGER</span>
        <span class="person-rule"></span>
      </div>
    </div>

    <ul class="contact-list">
      <li>
        <svg viewBox="0 0 24 24" aria-hidden="true"><path d="M6.6 10.8a15.1 15.1 0 0 0 6.6 6.6l2.2-2.2c.3-.3.7-.4 1-.2 1.1.4 2.3.6 3.6.6.6 0 1 .4 1 1V20c0 .6-.4 1-1 1A17 17 0 0 1 3 4c0-.6.4-1 1-1h3.5c.6 0 1 .4 1 1 0 1.3.2 2.5.6 3.6.1.3 0 .7-.2 1z"/></svg>
        555.214.3810
      </li>
      <li>
        <svg viewBox="0 0 24 24" aria-hidden="true"><path d="M7 2h10v5H7zM4 8h16a2 2 0 0 1 2 2v7h-4v5H6v-5H2v-7a2 2 0 0 1 2-2zm4 9v3h8v-3z"/></svg>
        555.214.3871
      </li>
      <li>
        <svg viewBox="0 0 24 24" aria-hidden="true"><path d="M2 5h20v14H2zm2 2v.4l8 5.2 8-5.2V7zm0 2.8V17h16V9.8l-8 5.2z"/></svg>
        dwhitcombe@tessarotech.com
      </li>
    </ul>

    <address class="address">
      1180 W 54th ST<br>
      Larkfield Indiana 46099<br>
      <span class="web">www.tessarotech.com</span>
    </address>

    <svg class="band" viewBox="0 0 615 13" preserveAspectRatio="none" aria-hidden="true">
      <polygon points="0,0 402,0 398,13 0,13" fill="var(--navy)"/>
      <polygon points="406,0 615,0 615,13 402,13" fill="var(--sky)"/>
    </svg>
  </section>

  <section class="card card-back">
    <div class="emblem" role="img" aria-label="Brand emblem illustration"></div>
    <p class="back-web">www.tessarotech.com</p>
  </section>
</body>
</html>
```